Yonder Book Cover for a new author entering the writing space

Design a stunning, eye catching book cover for a Christian Book. Front, back & spine needs to be designed. I am currently reviewing the final draft so the cover will need to be finalized for print once I have the number of pages and the back cover information.

Book Title: Yonder
Book Subtitle: Discovering your true self in Christ.

Author Name: Dr. Calvin Maddox

Target Market(s)

Christian readers

Industry/Entity Type

Christian

Colors

Designer to choose colors to be used in the design.

Requirements
Must have
• Bold Title
• Bold Author
• Bold color
• Clean design
Should not have
• No angel wings
• No hands coming out of heaven
• No doves

```html
<!DOCTYPE html>
<html lang="en">
<head>
<meta charset="utf-8">
<title>Yonder — Book Cover</title>
<link rel="stylesheet" href="https://fonts.googleapis.com/css2?family=Great+Vibes&family=Carlito:ital,wght@0,400;1,400&display=swap">
<style>
  :root {
    --navy-deep: #1f2d42;
    --navy: #2b3c55;
    --glow-mid: #7f8fa8;
    --glow-core: #d3dae6;
    --title: #cfd3e6;
    --title-shadow: rgba(20, 28, 45, 0.6);
    --text-light: #ffffff;
    --lotus: #c184e6;
    --lotus-deep: #8d4fc4;
    --water: #3a4d6a;
  }
  html, body {
    margin: 0;
    padding: 0;
    width: 960px;
    height: 1200px;
    overflow: hidden;
    background: var(--navy-deep);
  }
  .cover {
    position: relative;
    width: 960px;
    height: 1200px;
    overflow: hidden;
    background:
      radial-gradient(ellipse 420px 520px at 50% 62%, var(--glow-core) 0%, var(--glow-mid) 32%, var(--navy) 70%, var(--navy-deep) 100%);
  }
  .cover__title {
    position: absolute;
    top: 120px;
    left: 0;
    width: 100%;
    margin: 0;
    text-align: center;
    font-family: "Great Vibes", cursive;
    font-weight: 400;
    font-size: 250px;
    line-height: 1;
    color: var(--title);
    text-shadow: 3px 4px 4px var(--title-shadow);
  }
  .cover__subtitle {
    position: absolute;
    top: 486px;
    left: 0;
    width: 100%;
    margin: 0;
    text-align: center;
    font-family: "Carlito", sans-serif;
    font-style: italic;
    font-size: 52px;
    color: var(--text-light);
  }
  .cover__artwork {
    position: absolute;
    left: 190px;
    top: 640px;
    width: 580px;
    height: 380px;
    border-radius: 50%;
    background:
      radial-gradient(ellipse 170px 100px at 50% 58%, var(--lotus) 0%, var(--lotus-deep) 55%, rgba(141, 79, 196, 0) 100%),
      radial-gradient(ellipse 290px 90px at 50% 82%, var(--water) 0%, rgba(58, 77, 106, 0) 100%);
  }
  .cover__author {
    position: absolute;
    top: 1090px;
    left: 0;
    width: 100%;
    margin: 0;
    text-align: center;
    font-family: "Carlito", sans-serif;
    font-size: 56px;
    color: var(--text-light);
  }
</style>
</head>
<body>
  <main class="cover">
    <h1 class="cover__title">Yonder</h1>
    <p class="cover__subtitle">Discovering your true self in Christ</p>
    <div class="cover__artwork" role="img" aria-label="A glowing violet lotus flower floating on rippling dark water, with small sparkles of light rising above it"></div>
    <p class="cover__author">Dr. Calvin Maddox</p>
  </main>
</body>
</html>
```